Business Card Design for Concierge business

Hi. I would like to have an elegant, smart business card for my concierge business, called Harbor Concierge. The services I provide are mail management, dog walking, cleaning, car, stylist, personal shopper, running errands, property management, event planning. I was thinking to add my picture but I would like to see options without it as well, if possible.

Thank you.

Business Card Details:
*Designers are to solely use contact information for the business card design. This is not to be used to contact the customer*

Name: Tamsin Heller
mail: quaylineerrands@mailvora.net
Phone: 305-482-9167

Target Market(s)

vacation home owners

Industry/Entity Type

Business

Font styles to use
Serif

Colors

Designer to choose colors to be used in the design.

Requirements
Nice to have
• Could use icons that describe the services I provide for example car, house, key, shopping cart, shopping bags, envelope, champagne glasses, phone, dog etc.

```html
<!DOCTYPE html>
<html lang="en">
<head>
<meta charset="utf-8">
<title>Harbor Concierge — Business Card</title>
<link rel="stylesheet" href="https://fonts.googleapis.com/css2?family=Playfair+Display:wght@400;700&family=Crimson+Text:wght@400;600&display=swap">
<style>
  :root {
    --page: #e9e9ec;
    --card-white: #ffffff;
    --royal: #34479f;
    --royal-deep: #27378c;
    --royal-light: #5a69c2;
    --gold: #c19a3c;
    --ink: #151515;
    --label: #f2f3fb;
  }
  * { margin: 0; padding: 0; box-sizing: border-box; }
  html, body { width: 1200px; height: 900px; overflow: hidden; }
  body {
    background: var(--page);
    display: flex; flex-direction: column; align-items: center; justify-content: center;
    gap: 60px;
  }
  .card {
    position: relative;
    width: 600px; height: 343px;
    box-shadow: 0 10px 28px rgba(0,0,0,.18);
    overflow: hidden;
  }
  .card-front {
    background: var(--card-white);
    display: flex; align-items: center; justify-content: center;
  }
  .brand-name {
    font-family: "Playfair Display", serif;
    font-weight: 400;
    font-size: 50px;
    line-height: 1.05;
    color: var(--royal);
    text-align: center;
  }
  .card-back {
    background:
      repeating-linear-gradient(-32deg, rgba(255,255,255,.07) 0 1px, transparent 1px 9px),
      linear-gradient(160deg, var(--royal-deep) 0%, var(--royal) 45%, var(--royal-light) 100%);
  }
  .back-fade {
    position: absolute; left: 0; right: 0; bottom: 0; height: 120px;
    background: linear-gradient(to bottom, rgba(255,255,255,0) 0%, rgba(255,255,255,.85) 45%, #fff 62%);
  }
  .service {
    position: absolute;
    width: 120px; margin-left: -60px;
    display: flex; flex-direction: column; align-items: center; gap: 5px;
  }
  .service-badge {
    width: 58px; height: 58px; border-radius: 50%;
    background: #fff; border: 3px solid var(--gold);
    display: flex; align-items: center; justify-content: center;
  }
  .service-badge svg { width: 34px; height: 34px; }
  .service-label {
    font-family: "Crimson Text", serif;
    font-size: 13px; color: var(--label); white-space: nowrap;
  }
  .contact-strip {
    position: absolute; left: 28px; right: 28px; bottom: 22px;
    display: flex; align-items: center; gap: 12px;
    font-family: "Crimson Text", serif; font-size: 15px; color: var(--ink);
  }
  .contact-name { font-family: "Playfair Display", serif; font-weight: 700; font-size: 15px; }
  .contact-divider { width: 1px; height: 16px; background: #a5a5a5; }
  .contact-item { display: flex; align-items: center; gap: 6px; }
  .contact-icon {
    width: 18px; height: 18px; border-radius: 50%; background: var(--royal);
    display: flex; align-items: center; justify-content: center;
  }
  .contact-icon svg { width: 11px; height: 11px; }
</style>
</head>
<body>

<section class="card card-front" aria-label="Card front">
  <h1 class="brand-name">Harbor<br>Concierge</h1>
</section>

<section class="card card-back" aria-label="Card back">
  <div class="back-fade"></div>

  <!-- row one -->
  <div class="service" style="left:80px; top:28px;">
    <div class="service-badge">
      <svg viewBox="0 0 24 24" fill="var(--gold)"><path d="M5 11l2-5h10l2 5h1v6h-2v2h-3v-2H9v2H6v-2H4v-6z"/><rect x="7.5" y="7.5" width="9" height="3.5" fill="#fff"/><circle cx="7.5" cy="14" r="1.3" fill="#fff"/><circle cx="16.5" cy="14" r="1.3" fill="#fff"/></svg>
    </div>
    <span class="service-label">Car</span>
  </div>
  <div class="service" style="left:190px; top:28px;">
    <div class="service-badge">
      <svg viewBox="0 0 24 24" fill="var(--gold)" stroke="var(--gold)" stroke-linecap="round">
        <rect x="6" y="10.5" width="11" height="4.5" rx="2" stroke="none"/>
        <circle cx="5.2" cy="9" r="2.4" stroke="none"/>
        <path d="M2.5 9.6h2" stroke-width="2"/>
        <path d="M4.5 6.8l-.8 2" stroke-width="1.6"/>
        <path d="M7.5 14v5M10 14v5M14 14v5M16 14v5" stroke-width="1.6"/>
        <path d="M16.8 11.5l2.2-3" stroke-width="1.5"/>
        <path d="M6 8.5L21 4" stroke-width="1" fill="none"/>
      </svg>
    </div>
    <span class="service-label">Dog walking</span>
  </div>
  <div class="service" style="left:300px; top:28px;">
    <div class="service-badge">
      <svg viewBox="0 0 24 24" fill="var(--gold)" stroke="var(--gold)" stroke-linecap="round">
        <circle cx="6" cy="5" r="1.3" stroke="none"/>
        <circle cx="9" cy="3.8" r="1" stroke="none"/>
        <circle cx="11.5" cy="5.2" r="1.4" stroke="none"/>
        <path d="M3 9h13l-1.6 10H4.6z" stroke="none"/>
        <path d="M4 9c0-4 11-4 11 0" fill="none" stroke-width="1.3"/>
        <path d="M21 4l-3.5 10" stroke-width="1.6"/>
        <path d="M15.5 13.5l4 1.3-1.5 5-4-1.4z" stroke="none"/>
      </svg>
    </div>
    <span class="service-label">Cleaning</span>
  </div>
  <div class="service" style="left:410px; top:28px;">
    <div class="service-badge">
      <svg viewBox="0 0 24 24" fill="none" stroke="var(--gold)" stroke-width="2" stroke-linejoin="round"><rect x="3" y="6" width="18" height="12" rx="1"/><path d="M3 6l9 7 9-7M3 18l7-6M21 18l-7-6"/></svg>
    </div>
    <span class="service-label">Mail management</span>
  </div>
  <div class="service" style="left:520px; top:28px;">
    <div class="service-badge">
      <svg viewBox="0 0 24 24" fill="var(--gold)" stroke="var(--gold)" stroke-linecap="round">
        <rect x="10.8" y="1.5" width="2.4" height="2.5" rx="1" stroke="none"/>
        <path d="M7 5h10l-1 3.5 1 4.5-1.5 3h-7L7 13l1-4.5z" stroke="none"/>
        <path d="M12 16v5.5M8.5 21.5h7" stroke-width="1.8"/>
      </svg>
    </div>
    <span class="service-label">Stylist</span>
  </div>

  <!-- row two -->
  <div class="service" style="left:135px; top:128px;">
    <div class="service-badge">
      <svg viewBox="0 0 24 24" fill="none" stroke="var(--gold)" stroke-width="2" stroke-linecap="round" stroke-linejoin="round"><path d="M2 4h3l2.5 11h11l2-8H6.3"/><circle cx="9" cy="19" r="1.5" fill="var(--gold)"/><circle cx="17" cy="19" r="1.5" fill="var(--gold)"/></svg>
    </div>
    <span class="service-label">Personal shopper</span>
  </div>
  <div class="service" style="left:245px; top:128px;">
    <div class="service-badge">
      <svg viewBox="0 0 24 24" fill="none" stroke="var(--gold)" stroke-width="2.4" stroke-linecap="round" stroke-linejoin="round">
        <circle cx="15.5" cy="4" r="2.2" fill="var(--gold)" stroke="none"/>
        <path d="M14 7.5l-3 6"/>
        <path d="M8 8.5l3.5-1.5 3 3 3 .5"/>
        <path d="M11 13.5l3.5 3-1 4.5"/>
        <path d="M11 13.5l-2.5 3.5H4.5"/>
      </svg>
    </div>
    <span class="service-label">Running errands</span>
  </div>
  <div class="service" style="left:355px; top:128px;">
    <div class="service-badge">
      <svg viewBox="0 0 24 24" fill="var(--gold)"><path d="M12 3l10 9h-3v9h-5v-6h-4v6H5v-9H2z"/></svg>
    </div>
    <span class="service-label">Property management</span>
  </div>
  <div class="service" style="left:465px; top:128px;">
    <div class="service-badge">
      <svg viewBox="0 0 24 24" fill="none" stroke="var(--gold)" stroke-width="1.8" stroke-linecap="round" stroke-linejoin="round"><path d="M5 5h5l-1 6a2 2 0 0 1-3 0zM7.5 12v7M5.5 19h4M14 5h5l-1 6a2 2 0 0 1-3 0zM16.5 12v7M14.5 19h4"/></svg>
    </div>
    <span class="service-label">Event planning</span>
  </div>

  <div class="contact-strip">
    <span class="contact-name">Tamsin Heller</span>
    <span class="contact-divider"></span>
    <span class="contact-item">
      <span class="contact-icon"><svg viewBox="0 0 24 24" fill="none" stroke="#fff" stroke-width="3"><rect x="3" y="6" width="18" height="12"/><path d="M3 6l9 7 9-7"/></svg></span>
      quaylineerrands@mailvora.net
    </span>
    <span class="contact-divider"></span>
    <span class="contact-item">
      <span class="contact-icon"><svg viewBox="0 0 24 24" fill="#fff"><path d="M6.6 10.8a15 15 0 0 0 6.6 6.6l2.2-2.2a1 1 0 0 1 1-.25 11.4 11.4 0 0 0 3.6.6 1 1 0 0 1 1 1V20a1 1 0 0 1-1 1A17 17 0 0 1 3 4a1 1 0 0 1 1-1h3.5a1 1 0 0 1 1 1c0 1.25.2 2.45.6 3.6a1 1 0 0 1-.25 1z"/></svg></span>
      305-482-9167
    </span>
  </div>
</section>

</body>
</html>
```